Packaging and logo design for washcloths

We are a company manufacturing towels and washcloths for babies.We are planning to get into e-commerce business with washcloths for babies made out of 100% Rayon made from Bamboo.We would like to see a logo design that symbolizes the perfection of the nature and a packaging design that gives mothers the feeling of cleanliness,pureness, softness and eco-friendliness. The packaging will include 6 items, each washcloth is 10x10 inches. The details will be discussed with the designer.

Looking for a clean and neat design that will attract the buyers which will also emphasize the fact that it is made out of highest quality rayon from bamboo that don’t irritate sensitive and delicate skin. I am planning to outsource more work (website,flyers, pictures and social media related stuff) to the designers who does the best job for this packaging project .

Target Market(s)

E-commerce customers, mothers,

Colors

Designer to choose colors to be used in the design.

Requirements
Must have
• clean and stylish look that should emphasize the fact that the product is 100% organic bamboo, eco-friendly,premium ultra soft, perfect for delicate and sensitive skin and 100% natural.Kraft paper packaging might be more suitable for an eco-friendly, bamboo based product.
Nice to have
• Packaging dimensions of our first competitors is 8.3 x 5.6 x 1.4 inches and the second one is 8.2 x 5.8 x 1.5 inches therefore; the final product should be designed according to these dimensions keeping in mind that each box will have 6 towels in it.

```html
<!DOCTYPE html>
<html lang="en">
<head>
<meta charset="utf-8">
<title>Organic Bamboo Washcloth Box – Front Panel</title>
<link rel="stylesheet" href="https://fonts.googleapis.com/css2?family=Oswald:wght@500;700&family=Montserrat:wght@400;500&display=swap">
<style>
  :root {
    --stage: #f3f3f5;
    --kraft: #cdaa78;
    --kraft-light: #d6b785;
    --kraft-dark: #bf9a66;
    --ink: #2b2b2b;
    --bamboo-dark: #8a9a5b;
    --bamboo-light: #b7b57a;
    --leaf: #9bb43a;
    --cloth-light: #f4f4f2;
    --cloth-shadow: #d9d9d6;
    --shelf: #b8874f;
    --badge: #2e2e2e;
    --badge-text: #ffffff;
  }
  * { box-sizing: border-box; margin: 0; padding: 0; }
  html, body {
    width: 1200px; height: 829px; overflow: hidden;
    background: var(--stage);
  }
  .box-front {
    position: absolute; left: 41px; top: 40px;
    width: 1117px; height: 750px;
    background: linear-gradient(135deg, var(--kraft-light), var(--kraft) 55%, var(--kraft-dark));
    overflow: hidden;
  }
  .bamboo-band {
    position: absolute; top: 0; height: 750px;
    background: linear-gradient(90deg, var(--bamboo-light), var(--bamboo-dark) 35%, var(--bamboo-light) 60%, var(--bamboo-dark));
    opacity: 0.75;
  }
  .bamboo-band--left { left: 0; width: 197px; }
  .bamboo-band--right { right: 0; width: 205px; }
  .product-window { position: absolute; left: 0; top: 0; }
  .title {
    position: absolute; left: 195px; top: 52px; width: 742px;
    font-family: 'Oswald', sans-serif; font-weight: 700;
    font-size: 62px; line-height: 72px; color: var(--ink);
    letter-spacing: 0.5px; white-space: nowrap;
    border-bottom: 2px solid var(--ink);
    padding-bottom: 4px;
  }
  .features { position: absolute; left: 57px; top: 192px; list-style: none; }
  .feature {
    display: flex; align-items: center; height: 67px;
    font-family: 'Oswald', sans-serif; font-weight: 500;
    font-size: 33px; color: var(--ink); letter-spacing: 0.2px;
  }
  .feature svg { width: 50px; height: 50px; margin-right: 14px; flex: none; }
  .pack-count {
    position: absolute; left: 74px; top: 650px;
    font-family: 'Montserrat', sans-serif; font-weight: 400;
    font-size: 52px; color: var(--ink);
  }
  .size-badge {
    position: absolute; left: 991px; top: 648px;
    width: 100px; height: 100px; border-radius: 50%;
    background: var(--badge); color: var(--badge-text);
    display: flex; flex-direction: column; align-items: center; justify-content: center;
    font-family: 'Montserrat', sans-serif; line-height: 1;
  }
  .size-badge .each { font-size: 15px; margin-bottom: 3px; }
  .size-badge .dims { font-size: 26px; font-weight: 500; }
  .size-badge .unit { font-size: 19px; margin-top: 2px; }
</style>
</head>
<body>
  <main class="box-front">
    <div class="bamboo-band bamboo-band--left" role="img" aria-label="Illustration of green bamboo stalks with leaves"></div>
    <div class="bamboo-band bamboo-band--right" role="img" aria-label="Illustration of green bamboo stalks with leaves"></div>

    <svg class="product-window" width="1117" height="750" viewBox="0 0 1117 750">
      <defs>
        <linearGradient id="cloth" x1="0" y1="0" x2="1" y2="0">
          <stop offset="0" stop-color="var(--cloth-shadow)"/>
          <stop offset="0.3" stop-color="var(--cloth-light)"/>
          <stop offset="0.6" stop-color="var(--cloth-shadow)"/>
          <stop offset="0.8" stop-color="var(--cloth-light)"/>
          <stop offset="1" stop-color="var(--cloth-shadow)"/>
        </linearGradient>
      </defs>
      <path role="img" aria-label="Window showing rolled white bamboo washcloths"
            d="M367 640 C380 420 470 250 640 208 L1039 208 L1039 590 Q1039 640 989 640 Z"
            fill="url(#cloth)"/>
      <rect x="369" y="628" width="655" height="10" fill="var(--shelf)"/>
    </svg>

    <h1 class="title">100% organic bamboo wascloth</h1>

    <ul class="features">
      <li class="feature">
        <svg viewBox="0 0 50 50"><circle cx="25" cy="25" r="22" fill="none" stroke="var(--ink)" stroke-width="2.5"/><line x1="10" y1="40" x2="40" y2="10" stroke="var(--ink)" stroke-width="2.5"/><circle cx="24" cy="28" r="6" fill="none" stroke="var(--ink)" stroke-width="2"/></svg>
        100% ORGANIC&nbsp; BAMBOO
      </li>
      <li class="feature">
        <svg viewBox="0 0 50 50"><circle cx="25" cy="25" r="22" fill="none" stroke="var(--ink)" stroke-width="2.5"/><line x1="10" y1="40" x2="40" y2="10" stroke="var(--ink)" stroke-width="2.5"/><circle cx="20" cy="20" r="3" fill="var(--ink)"/><circle cx="30" cy="30" r="3" fill="var(--ink)"/><circle cx="18" cy="31" r="2" fill="var(--ink)"/></svg>
        FOR DELICATE &amp; SENSITIVE SKIN
      </li>
      <li class="feature">
        <svg viewBox="0 0 50 50"><circle cx="25" cy="25" r="22" fill="none" stroke="var(--ink)" stroke-width="2.5"/><line x1="25" y1="11" x2="25" y2="27" stroke="var(--ink)" stroke-width="2.5"/><path d="M19 22 L25 28 L31 22" fill="none" stroke="var(--ink)" stroke-width="2.5"/><line x1="13" y1="32" x2="37" y2="32" stroke="var(--ink)" stroke-width="2"/><line x1="15" y1="37" x2="35" y2="37" stroke="var(--ink)" stroke-width="2"/></svg>
        PREMIUM ULTRA SOFT
      </li>
      <li class="feature">
        <svg viewBox="0 0 50 50"><circle cx="25" cy="25" r="22" fill="none" stroke="var(--ink)" stroke-width="2.5"/><path d="M15 35 C15 20 25 14 36 14 C36 26 30 35 15 35 Z" fill="var(--ink)"/></svg>
        ECO FRIENDLY
      </li>
    </ul>

    <p class="pack-count">6 PCS</p>

    <div class="size-badge">
      <span class="each">EACH</span>
      <span class="dims">10x10</span>
      <span class="unit">inch</span>
    </div>
  </main>
</body>
</html>
```